Website design for an edge protection barrier system

- The design must be based around the attached HPID (home page information design) called CODE HPID. I've attached Word and PDF versions - these are the same. The table boxes are just for approximate placement of information – you DON'T have to make it look exactly like this. All fonts used in the HPID are only examples - you can use any Google font you wish.

- Information only is in orange text. Copy to go on the design in black text. Some instructions are in the HPID. Please be creative!

- The design needs to be modern. Colours are to be black and white with orange ...like the logo colours.

- I've provided the images for the galleries - they are labelled and will match the name in the HPID.

- Examples of some websites that have great design... don't copy them please but they are similar in look to what we are after....
http://wandertrail.co.nz/
http://www.lumfuel.co.nz/
http://www.tolbertwade.co.nz/

Width of content will be 1100 pixels when implemented as a web page. Header height (without nav bar) 150-160 pixels.

If your design is chosen the winning PSD file will have to be provided as follows…
1. Canvas size of 2000px x 2000px - 72ppi in Adobe Photoshop (CS5 compatible)
2. Width of content section is 1100px wide - centered in the canvas
3. Any button rollovers/hovers in the PSD as hidden layers.
4. All fonts used must be Google fonts (except for the fonts in the header at the top of the page).
5. You will need to supply the chosen home page plus one example page (example page as a style guide for how all other pages will look). Example page is only the header and navigational bar at the top, an empty sector in the middle with a column (180 px wide) which can be left or right aligned which means the main sector is 920 pixels wide, and then the footer at the bottom of the page
Updates

Hi all, As per the HPID for the main image gallery you must use: File 7: edge protection systems for new houses hp wednesday, 17 december 2014 04:35:4112 AND File 9: e bracket for new home edge protection hp wednesday, 17 december 2014 04:35:4111 Use these images so they fit next to each other with the words: Edge protection systems for new houses with timber or aluminium rails (These words must be used either on or above or below the gallery) What we are looking for is a clean modern layout of the home page. The images supplied must be used please. Thank you.

Our office is closed over the New Year holiday season so decisions on designs may be delayed.

```html
<!DOCTYPE html>
<html lang="en">
<head>
<meta charset="utf-8">
<title>Ridgeline Edge Protection</title>
<link href="https://fonts.googleapis.com/css2?family=Dosis:wght@400;500&display=swap" rel="stylesheet">
<style>
  :root {
    --orange: #e55e27;
    --black: #151515;
    --white: #ffffff;
    --label-bg: rgba(30, 30, 30, 0.82);
    --caption-bg: rgba(255, 255, 255, 0.88);
  }
  * { margin: 0; padding: 0; box-sizing: border-box; }
  html, body {
    width: 1200px; height: 900px; overflow: hidden;
    background: var(--white);
    font-family: "Dosis", sans-serif;
  }
  .site-header {
    position: absolute; left: 0; top: 0; width: 1200px; height: 201px;
    background: var(--orange);
  }
  .brand {
    position: absolute; left: 50px; top: 22px;
    display: flex; align-items: center; gap: 12px;
    color: var(--white); font-size: 34px; font-weight: 500;
  }
  .brand-square { width: 34px; height: 34px; background: var(--white); }
  .tagline {
    position: absolute; right: 50px; top: 45px;
    color: var(--white); font-size: 25px; font-weight: 400; text-align: right;
  }
  .phone {
    position: absolute; right: 50px; top: 80px;
    color: var(--white); font-size: 35px; font-weight: 400; letter-spacing: 0.5px;
  }
  .main-nav {
    position: absolute; left: 50px; top: 160px; width: 1100px; height: 41px;
    background: var(--black);
    display: flex; justify-content: space-between; align-items: center;
    padding-right: 26px;
  }
  .main-nav a {
    color: var(--white); text-decoration: none; font-size: 18px; font-weight: 400;
  }
  .main-nav a.active {
    background: var(--white); color: var(--black);
    width: 106px; height: 41px; margin-top: -6px; padding-top: 6px;
    display: flex; align-items: center; justify-content: center;
    border-bottom: 3px solid var(--black);
  }
  .hero {
    position: absolute; left: 0; top: 201px; width: 1200px; height: 418px;
    background: linear-gradient(180deg, #8f969f 0%, #b3b6b9 35%, #c79e74 55%, #a9825c 72%, #d8d9db 100%);
  }
  .hero-caption {
    position: absolute; left: 478px; top: 470px; width: 670px; height: 48px;
    background: var(--caption-bg);
    color: var(--orange); font-size: 23px; font-weight: 400;
    display: flex; align-items: center; justify-content: center;
  }
  .feature-cards {
    position: absolute; left: 50px; top: 660px; width: 1100px;
    display: flex; justify-content: space-between;
  }
  .feature-card {
    position: relative; width: 340px; height: 198px;
    box-shadow: 0 2px 6px rgba(0,0,0,0.25);
  }
  .card-soffit { background: linear-gradient(135deg, #d4a82a 0%, #e8c23a 50%, #4e8a52 100%); }
  .card-truss { background: linear-gradient(135deg, #8a4b3c 0%, #c9c9cc 45%, #dba72c 100%); }
  .card-reroof { background: linear-gradient(180deg, #3f7ec9 0%, #6ea0d8 45%, #e8ecef 100%); }
  .card-label {
    position: absolute; left: 0; top: 78px; width: 100%; height: 43px;
    background: var(--label-bg);
    color: var(--white); font-size: 25px; font-weight: 400;
    display: flex; align-items: center; justify-content: center;
  }
</style>
</head>
<body>
  <header class="site-header">
    <div class="brand"><span class="brand-square"></span>Ridgeline</div>
    <p class="tagline">Innovative edge protection system for the building industry-NZ wide</p>
    <p class="phone">0800 RIDGEL | 0800 743435</p>
    <nav class="main-nav">
      <a class="active" href="#">Home</a>
      <a href="#">About Us</a>
      <a href="#">Edge Protection Systems</a>
      <a href="#">Safety</a>
      <a href="#">Testimonials</a>
      <a href="#">Gallery</a>
      <a href="#">Downloads/Videos</a>
      <a href="#">Quote/Contact</a>
    </nav>
  </header>

  <div class="hero" role="img" aria-label="New house under construction with timber roof trusses and yellow brackets holding red edge protection rails, cloudy sky"></div>
  <p class="hero-caption">Edge protection systems for new houses with timber or aluminium rails</p>

  <section class="feature-cards">
    <div class="feature-card card-soffit" role="img" aria-label="Close-up of yellow soffit mount bracket">
      <span class="card-label">New Build Soffit Mount</span>
    </div>
    <div class="feature-card card-truss" role="img" aria-label="Close-up of yellow truss mount bracket on timber truss">
      <span class="card-label">New Build Truss Mount</span>
    </div>
    <div class="feature-card card-reroof" role="img" aria-label="Edge protection rails on a house roof during re-roofing">
      <span class="card-label">Re-roof</span>
    </div>
  </section>
</body>
</html>
```